Private Maths Tuition Flyer based in London

I am opening up a new Maths tuition centre in North West London. The flyer will be delivered to over 8,000 homes within the immediate vicinity. The design should be suitable to be printed on an A5 sheet and read in a portrait orientation.

The flyer should include the following:

The headline statement should be "Private Maths Tuition"

Secondary headline statement is the following "GCSE, A-Levels, 11 Plus exams"

Some of service offerings/selling points are:

- Free first session
- Monthly Feedback reports
- Free support outside of sessions
- Clear Target grades
- Personalised Lesson plans
- Tangible Results

Another statement that should be featured is "Book your free session by visiting www.lernova.co.uk" or something similar to that.

"Contact Details:
020 4719 8263
enquiries@lernova.co.uk"

"Address:
Kelbridge Business and Innovation Centre
Ashvale Court
Wrenfield Road
HA4 9QD"

Attached you'll see a logo which should be included and also a map of where we are. I am open to new images for the map if you guys have any, rather than a screen shot from google maps but it should be clear to see.

I would like the content above to be displayed in a clear and concise manner that is easy to read. You have creative license on where this information should be displayed and where the images should be but on the whole it should look aesthetically pleasing on the eye.

Target Market(s)

Students, Parents. Parents who want maths tutors.

Industry/Entity Type

Tutoring

Font styles to use
Sans Serif

Requirements
Must have
• *logo*
• Private Maths Tuition
• GCSE, A-Levels, 11 Plus exams
• - Free first session
• - Monthly Feedback reports
• - Free support outside of sessions
• - Clear Target grades
• - Personalised Lesson plans
• - Tangible Results
• Book your free session by visiting www.lernova.co.uk" or something similar to that.
• Contact Details:
• 020 4719 8263
• enquiries@lernova.co.uk
• Address (*with map*):
• Kelbridge Business and Innovation Centre
• Ashvale Court
• Wrenfield Road
• HA4 9QD
Nice to have
• similar colour scheme as the logo. creative background design.

```html
<!DOCTYPE html>
<html lang="en">
<head>
<meta charset="utf-8">
<title>Lernova – Private Maths Tuition Flyer</title>
<link rel="stylesheet" href="https://fonts.googleapis.com/css2?family=Saira:wght@600;700&family=Lato:wght@400;700&display=swap">
<style>
  :root {
    --blue: #1560b6;
    --blue-dark: #0e4d9c;
    --orange: #e8691b;
    --green: #6cb33f;
    --ink: #1e1e1e;
    --panel: #ececec;
    --page: #e4e4e4;
    --white: #ffffff;
  }
  * { box-sizing: border-box; margin: 0; padding: 0; }
  html, body {
    width: 1200px; height: 1013px; overflow: hidden;
    background: var(--page);
  }
  .flyer {
    position: absolute; left: 250px; top: 11px;
    width: 700px; height: 990px;
    background: var(--white);
    overflow: hidden;
    box-shadow: 0 4px 18px rgba(0,0,0,.18);
    font-family: "Lato", sans-serif;
    color: var(--ink);
  }
  .headline {
    position: absolute; top: 14px; left: 0; width: 100%;
    text-align: center;
    font-family: "Saira", sans-serif; font-weight: 700;
    font-size: 62px; line-height: 1; color: var(--blue);
    letter-spacing: .5px;
  }
  .subheadline {
    position: absolute; top: 86px; left: 0; width: 100%;
    text-align: center;
    font-weight: 700; font-size: 31px; color: var(--orange);
  }
  .photo {
    position: absolute; top: 110px; left: 0; width: 700px; height: 480px;
    background:
      linear-gradient(180deg, rgba(255,255,255,1) 0%, rgba(255,255,255,0) 14%),
      radial-gradient(ellipse at 45% 60%, #4f79b8 0%, rgba(79,121,184,0) 45%),
      linear-gradient(160deg, #f1e2bf 0%, #d9c49a 35%, #a9b4c6 60%, #6f86ad 100%);
  }
  .waves { position: absolute; left: 0; top: 0; width: 700px; height: 990px; }
  .col-left { position: absolute; left: 22px; top: 580px; width: 310px; }
  .col-right { position: absolute; left: 370px; top: 586px; width: 320px; }
  .divider {
    position: absolute; left: 332px; top: 592px; width: 3px; height: 236px;
    background: linear-gradient(180deg, rgba(80,80,80,0), #8a8a8a 20%, #8a8a8a 80%, rgba(80,80,80,0));
  }
  .section-title {
    font-family: "Saira", sans-serif; font-weight: 700;
    color: var(--blue); font-size: 28px; line-height: 1.25;
  }
  .offerings { list-style: none; margin-top: 4px; }
  .offerings li {
    display: flex; align-items: center; gap: 8px;
    font-size: 18.5px; height: 31.5px;
  }
  .icon { width: 18px; height: 18px; flex: none; }
  .address { margin-top: 2px; }
  .address-lines { display: flex; gap: 8px; margin-top: 2px; font-size: 18.5px; line-height: 22px; }
  .address-lines strong { font-weight: 700; }
  .book { line-height: 1.25; }
  .contact-row {
    display: flex; align-items: center; gap: 14px;
    font-size: 21px; margin-top: 6px; padding-left: 12px;
  }
  .contact-title { margin-top: 14px; }
  .map {
    position: absolute; left: 267px; top: 823px; width: 166px; height: 166px;
    border-radius: 50%;
    border: 4px solid var(--orange);
    box-shadow: inset 0 0 0 4px var(--white), inset 0 0 0 7px var(--blue);
    background: radial-gradient(circle at 35% 65%, #cfe0c0 0%, #dfe6d8 30%, #eceee9 60%);
  }
  .brand {
    position: absolute; left: 490px; top: 880px;
    font-family: "Lato", sans-serif; font-weight: 700;
    font-size: 46px; color: var(--orange); letter-spacing: .5px;
  }
  .footer-line { position: absolute; left: 0; bottom: 16px; width: 100%; height: 2px; background: var(--blue); }
  .footer-band { position: absolute; left: 0; bottom: 0; width: 100%; height: 12px; background: var(--blue); }
</style>
</head>
<body>
  <div class="flyer">
    <div class="photo" role="img" aria-label="Photograph of secondary-school students studying together around a table with laptops and tablets, a tutor working in the background"></div>

    <svg class="waves" viewBox="0 0 700 990" aria-hidden="true">
      <defs>
        <linearGradient id="panelGrad" x1="0" y1="0" x2="0" y2="1">
          <stop offset="0" stop-color="#ffffff"/>
          <stop offset="1" stop-color="#e6e6e6"/>
        </linearGradient>
      </defs>
      <path d="M0,430 C150,440 280,520 400,548 S620,530 700,460 L700,990 L0,990 Z" fill="var(--blue)"/>
      <path d="M0,498 C150,473 280,533 400,553 S620,548 700,528" fill="none" stroke="#ffffff" stroke-width="5"/>
      <path d="M0,505 C150,480 280,540 400,560 S620,555 700,535 L700,990 L0,990 Z" fill="var(--orange)"/>
      <path d="M0,580 C80,552 220,548 400,572 S620,585 700,575 L700,990 L0,990 Z" fill="url(#panelGrad)"/>
    </svg>

    <h1 class="headline">Private Maths Tuition</h1>
    <p class="subheadline">GCSE, A-Levels, 11 Plus exams</p>

    <div class="divider"></div>

    <section class="col-left">
      <h2 class="section-title">Service Offerings</h2>
      <ul class="offerings">
        <li><svg class="icon" viewBox="0 0 18 18"><path d="M1,4 C8,1 16,4 17,15 C9,15 3,11 1,4 Z" fill="var(--green)"/></svg>Free first session</li>
        <li><svg class="icon" viewBox="0 0 18 18"><path d="M1,4 C8,1 16,4 17,15 C9,15 3,11 1,4 Z" fill="var(--green)"/></svg>Monthly Feedback reports</li>
        <li><svg class="icon" viewBox="0 0 18 18"><path d="M1,4 C8,1 16,4 17,15 C9,15 3,11 1,4 Z" fill="var(--green)"/></svg>Free support outside of sessions</li>
        <li><svg class="icon" viewBox="0 0 18 18"><path d="M1,4 C8,1 16,4 17,15 C9,15 3,11 1,4 Z" fill="var(--green)"/></svg>Clear Target grades</li>
        <li><svg class="icon" viewBox="0 0 18 18"><path d="M1,4 C8,1 16,4 17,15 C9,15 3,11 1,4 Z" fill="var(--green)"/></svg>Personalised Lesson plans</li>
        <li><svg class="icon" viewBox="0 0 18 18"><path d="M1,4 C8,1 16,4 17,15 C9,15 3,11 1,4 Z" fill="var(--green)"/></svg>Tangible Results</li>
      </ul>

      <div class="address">
        <h2 class="section-title">Address:</h2>
        <div class="address-lines">
          <svg class="icon" viewBox="0 0 18 18"><path d="M9,1 C5,1 3,4 3,7 C3,11 9,17 9,17 C9,17 15,11 15,7 C15,4 13,1 9,1 Z" fill="var(--green)"/><circle cx="9" cy="7" r="2.3" fill="#fff"/></svg>
          <p><strong>Kelbridge Business and<br>Innovation Centre</strong><br>Ashvale Court<br>Wrenfield Road<br>HA4 9QD</p>
        </div>
      </div>
    </section>

    <section class="col-right">
      <h2 class="section-title book">Book your<br>free session by visiting</h2>
      <p class="contact-row">
        <svg class="icon" viewBox="0 0 18 18"><circle cx="9" cy="9" r="7.5" fill="var(--green)"/><path d="M4,6 C6,5 7,8 9,7 C10,9 8,10 9,12 C7,13 5,10 4,6 Z M11,4 C13,5 15,7 14,10 C12,9 12,6 11,4 Z" fill="#fff"/></svg>
        www.lernova.co.uk
      </p>
      <h2 class="section-title contact-title">Contact Details:</h2>
      <p class="contact-row">
        <svg class="icon" viewBox="0 0 18 18"><path d="M4,1 L7,1 L8,5 L6,7 C7,10 8,11 11,12 L13,10 L17,11 L17,14 C17,16 15,17 13,17 C7,16 2,11 1,5 C1,3 2,1 4,1 Z" fill="var(--green)"/></svg>
        020 4719 8263
      </p>
      <p class="contact-row">
        <svg class="icon" viewBox="0 0 18 18"><rect x="1" y="4" width="16" height="11" fill="var(--green)"/><path d="M1,4 L9,10 L17,4" fill="none" stroke="#fff" stroke-width="1.4"/></svg>
        enquiries@lernova.co.uk
      </p>
    </section>

    <div class="map" role="img" aria-label="Street map showing the location of the tuition centre"></div>

    <div class="brand">Lernova</div>

    <div class="footer-line"></div>
    <div class="footer-band"></div>
  </div>
</body>
</html>
```